Brake Test Training for Coal Mining

We offer Brake Test Training for Coal Mine workers. It's a legislative requirement that workers who are tasked with performing brake testing have certain competencies to do so. We test Light Vehicles and trailers, Heavy Vehicles and Mobile Mining Equipment like Graders, Scrapers and Dump Trucks.

```html
<!DOCTYPE html>
<html lang="en">
<head>
<meta charset="utf-8">
<title>Brake Test Training Banners</title>
<link rel="stylesheet" href="https://fonts.googleapis.com/css2?family=Inter+Tight:wght@500;600;700;800;900&display=swap">
<style>
  :root {
    --page-bg: #c4d4ea;
    --navy: #22377d;
    --navy-deep: #1c2d6b;
    --navy-mid: #2c4a9c;
    --yellow: #fcc800;
    --white: #ffffff;
    --black: #000000;
    --ink-navy: #26347a;
    --truck-orange: #b8651c;
    --truck-dark: #3a2612;
  }
  * { margin: 0; padding: 0; box-sizing: border-box; }
  html, body {
    width: 769px; height: 1200px; overflow: hidden;
    background: var(--page-bg);
    font-family: "Inter Tight", Arial, sans-serif;
  }
  .banner-set { position: relative; width: 769px; height: 1200px; }
  .banner {
    position: absolute; left: 31px; width: 707px; height: 346px;
    overflow: hidden;
    box-shadow: 0 4px 14px rgba(40, 60, 110, 0.25);
  }
  .banner--navy { top: 38px; }
  .banner--black { top: 428px; }
  .banner--white { top: 817px; }

  .banner__backdrop {
    position: absolute; inset: 0;
    background:
      radial-gradient(ellipse 180px 160px at 440px 110px, rgba(90, 110, 170, 0.45), transparent 70%),
      linear-gradient(180deg, var(--navy) 0%, var(--navy-mid) 100%);
  }
  .banner__truck {
    position: absolute; left: 464px; top: 0; width: 243px; height: 254px;
    background:
      radial-gradient(ellipse 60px 40px at 150px 100px, rgba(255, 220, 150, 0.7), transparent 70%),
      linear-gradient(160deg, #d9892a 0%, var(--truck-orange) 40%, var(--truck-dark) 100%);
    -webkit-mask-image: linear-gradient(90deg, transparent 0%, #000 28%);
    mask-image: linear-gradient(90deg, transparent 0%, #000 28%);
  }

  .brand {
    position: absolute; left: 54px; top: 32px;
    display: flex; align-items: center; gap: 10px;
  }
  .brand__dot {
    width: 34px; height: 34px; border-radius: 50%;
    border: 3px solid var(--white);
  }
  .brand__name {
    color: var(--white); font-weight: 800; font-size: 14px;
    line-height: 1.15; letter-spacing: 0.3px; text-transform: uppercase;
    width: 130px;
  }

  .web-link {
    position: absolute; left: 242px; top: 30px; width: 260px; height: 39px;
    background: linear-gradient(90deg, var(--yellow) 0%, var(--yellow) 60%, rgba(252, 200, 0, 0) 100%);
    display: flex; align-items: center; padding-left: 9px; gap: 7px;
    color: var(--ink-navy); font-weight: 700; font-size: 18px; letter-spacing: -0.2px;
  }
  .web-link svg { width: 24px; height: 24px; }

  .headline {
    position: absolute; left: 45px; top: 88px;
    font-weight: 800; font-size: 48px; line-height: 41px;
    letter-spacing: -1.6px; text-transform: uppercase;
  }
  .headline__lead { display: block; color: var(--white); }
  .headline__accent { display: block; color: var(--yellow); }

  .intro {
    position: absolute; left: 54px; top: 186px; width: 440px;
    color: var(--white); font-weight: 600; font-size: 12.4px;
    line-height: 17.5px; letter-spacing: -0.25px; text-transform: uppercase;
  }

  .action-bar { position: absolute; left: 0; top: 254px; width: 707px; height: 92px; }
  .action-bar svg.action-bar__shapes { position: absolute; inset: 0; }
  .banner--navy .action-bar__band { fill: var(--navy-deep); }
  .banner--black .action-bar__band { fill: var(--black); }
  .banner--white .action-bar__band { fill: var(--white); }
  .action-bar__cta { fill: var(--yellow); }

  .phone {
    position: absolute; left: 28px; top: 22px;
    display: flex; align-items: center; gap: 16px;
  }
  .phone__icon {
    width: 48px; height: 48px; border-radius: 50%; background: var(--yellow);
    display: flex; align-items: center; justify-content: center;
  }
  .phone__icon svg { width: 26px; height: 26px; }
  .phone__icon path { fill: var(--navy-deep); }
  .banner--white .phone__icon path { fill: var(--white); }
  .phone__number {
    font-weight: 800; font-size: 47px; letter-spacing: -2px; color: var(--white);
  }
  .banner--white .phone__number { color: var(--ink-navy); }

  .apply {
    position: absolute; left: 466px; top: 24px;
    font-weight: 800; font-size: 37px; letter-spacing: -1px; color: var(--black);
  }
</style>
</head>
<body>
<main class="banner-set">

  <section class="banner banner--navy">
    <div class="banner__backdrop" role="img" aria-label="Blue-tinted photo of a mine worker in a hard hat over a city skyline"></div>
    <div class="banner__truck" role="img" aria-label="Photo of an orange prime mover truck with headlights on"></div>
    <div class="brand"><span class="brand__dot"></span><span class="brand__name">Summit Operator Training</span></div>
    <div class="web-link">
      <svg viewBox="0 0 24 24" fill="none" stroke="#26347a" stroke-width="1.6"><circle cx="12" cy="12" r="10"/><ellipse cx="12" cy="12" rx="4.5" ry="10"/><line x1="2" y1="12" x2="22" y2="12"/><line x1="3.5" y1="7" x2="20.5" y2="7"/><line x1="3.5" y1="17" x2="20.5" y2="17"/></svg>
      www.summitop.com.au
    </div>
    <h1 class="headline"><span class="headline__lead">Your Trusted</span><span class="headline__accent">Training Partner</span></h1>
    <p class="intro">We offer brake test training for coal mine workers. We test light vehicles and trailers, heavy vehicles and mobile mining equipment like graders, scrapers and dump trucks.</p>
    <div class="action-bar">
      <svg class="action-bar__shapes" viewBox="0 0 707 92"><polygon class="action-bar__band" points="0,0 427,0 408,92 0,92"/><polygon class="action-bar__cta" points="437,0 707,0 707,92 418,92"/></svg>
      <div class="phone">
        <span class="phone__icon"><svg viewBox="0 0 24 24"><path d="M6.6 10.8a15.1 15.1 0 0 0 6.6 6.6l2.2-2.2a1 1 0 0 1 1-.25 11.4 11.4 0 0 0 3.6.57 1 1 0 0 1 1 1V20a1 1 0 0 1-1 1A17 17 0 0 1 3 4a1 1 0 0 1 1-1h3.5a1 1 0 0 1 1 1c0 1.25.2 2.45.57 3.6a1 1 0 0 1-.25 1z"/></svg></span>
        <span class="phone__number">1300 555 019</span>
      </div>
      <span class="apply">APPLY NOW</span>
    </div>
  </section>

  <section class="banner banner--black">
    <div class="banner__backdrop" role="img" aria-label="Blue-tinted photo of a mine worker in a hard hat over a city skyline"></div>
    <div class="banner__truck" role="img" aria-label="Photo of an orange prime mover truck with headlights on"></div>
    <div class="brand"><span class="brand__dot"></span><span class="brand__name">Summit Operator Training</span></div>
    <div class="web-link">
      <svg viewBox="0 0 24 24" fill="none" stroke="#26347a" stroke-width="1.6"><circle cx="12" cy="12" r="10"/><ellipse cx="12" cy="12" rx="4.5" ry="10"/><line x1="2" y1="12" x2="22" y2="12"/><line x1="3.5" y1="7" x2="20.5" y2="7"/><line x1="3.5" y1="17" x2="20.5" y2="17"/></svg>
      www.summitop.com.au
    </div>
    <h2 class="headline"><span class="headline__lead">Your Trusted</span><span class="headline__accent">Training Partner</span></h2>
    <p class="intro">We offer brake test training for coal mine workers. We test light vehicles and trailers, heavy vehicles and mobile mining equipment like graders, scrapers and dump trucks.</p>
    <div class="action-bar">
      <svg class="action-bar__shapes" viewBox="0 0 707 92"><polygon class="action-bar__band" points="0,0 427,0 408,92 0,92"/><polygon class="action-bar__cta" points="437,0 707,0 707,92 418,92"/></svg>
      <div class="phone">
        <span class="phone__icon"><svg viewBox="0 0 24 24"><path d="M6.6 10.8a15.1 15.1 0 0 0 6.6 6.6l2.2-2.2a1 1 0 0 1 1-.25 11.4 11.4 0 0 0 3.6.57 1 1 0 0 1 1 1V20a1 1 0 0 1-1 1A17 17 0 0 1 3 4a1 1 0 0 1 1-1h3.5a1 1 0 0 1 1 1c0 1.25.2 2.45.57 3.6a1 1 0 0 1-.25 1z"/></svg></span>
        <span class="phone__number">1300 555 019</span>
      </div>
      <span class="apply">APPLY NOW</span>
    </div>
  </section>

  <section class="banner banner--white">
    <div class="banner__backdrop" role="img" aria-label="Blue-tinted photo of a mine worker in a hard hat over a city skyline"></div>
    <div class="banner__truck" role="img" aria-label="Photo of an orange prime mover truck with headlights on"></div>
    <div class="brand"><span class="brand__dot"></span><span class="brand__name">Summit Operator Training</span></div>
    <div class="web-link">
      <svg viewBox="0 0 24 24" fill="none" stroke="#26347a" stroke-width="1.6"><circle cx="12" cy="12" r="10"/><ellipse cx="12" cy="12" rx="4.5" ry="10"/><line x1="2" y1="12" x2="22" y2="12"/><line x1="3.5" y1="7" x2="20.5" y2="7"/><line x1="3.5" y1="17" x2="20.5" y2="17"/></svg>
      www.summitop.com.au
    </div>
    <h2 class="headline"><span class="headline__lead">Your Trusted</span><span class="headline__accent">Training Partner</span></h2>
    <p class="intro">We offer brake test training for coal mine workers. We test light vehicles and trailers, heavy vehicles and mobile mining equipment like graders, scrapers and dump trucks.</p>
    <div class="action-bar">
      <svg class="action-bar__shapes" viewBox="0 0 707 92"><polygon class="action-bar__band" points="0,0 427,0 408,92 0,92"/><polygon class="action-bar__cta" points="437,0 707,0 707,92 418,92"/></svg>
      <div class="phone">
        <span class="phone__icon"><svg viewBox="0 0 24 24"><path d="M6.6 10.8a15.1 15.1 0 0 0 6.6 6.6l2.2-2.2a1 1 0 0 1 1-.25 11.4 11.4 0 0 0 3.6.57 1 1 0 0 1 1 1V20a1 1 0 0 1-1 1A17 17 0 0 1 3 4a1 1 0 0 1 1-1h3.5a1 1 0 0 1 1 1c0 1.25.2 2.45.57 3.6a1 1 0 0 1-.25 1z"/></svg></span>
        <span class="phone__number">1300 555 019</span>
      </div>
      <span class="apply">APPLY NOW</span>
    </div>
  </section>

</main>
</body>
</html>
```